Rise As Captain Book Cover Design

Book Cover Design Brief
Book Title
Rise As Captain
Subtitle
The 12 Quiet Pillars of Remarkable Command
Author
Orwen Talbrisk
Overview
This book is about leadership that starts within.
Most leadership books focus on tactics or management strategies. This book focuses on the inner disciplines that create powerful leaders — mindset, integrity, focus, empathy, professionalism, honesty, and self-respect.
The tone of the book is bold, direct, confident, and transformational.
This is not a soft or corporate leadership book. It is a call to step up and become the leader you are capable of becoming.
The cover should feel:
• Powerful
• Professional
• Transformational
• Premium
• Memorable
Think best-selling leadership book, not a generic business book.
Target Audience
Business owners
Managers
Entrepreneurs
Team leaders
Professionals who want to grow as leaders
Most readers are ambitious professionals who want to level up their leadership and life.
Design Direction
The design should communicate:
Strength. Discipline. Leadership. Personal transformation.
Avoid cliché leadership visuals like:
• Handshakes
• Office buildings
• Corporate stock imagery
• Teams sitting around tables
The design should feel iconic, bold, and timeless.
Think about covers of successful leadership books such as:
Tiny Rituals
Total Custody
Won't Bend Now
Begin From Core
The 52 Codes of Sway
These covers are simple, powerful, and recognizable even at small sizes.
Typography
The title RISE AS CAPTAIN should be:
• Bold
• Strong
• Dominant on the cover
• Easy to read even at small sizes (important for Quillora thumbnails)
The subtitle should be clean and secondary to the title.
The overall typography should feel strong, modern, and premium.
Color Direction
Designers are free to explore colors, but the cover should feel strong and premium, not playful.
Colors that often work well for leadership books include:
Black
Gold
White
Deep blue
Dark red
High contrast and clarity are important.
Style
Preferred style:
• Clean
• Modern
• Minimal
• Strong contrast
Avoid clutter and overly busy designs.
The goal is to create a cover that feels powerful and professional at first glance.
Deliverables
Front cover design for a leadership book.
Final files should include:
• High resolution artwork
• Editable source files
• Print-ready version suitable for publishing
Goal of the Cover
When someone sees this book on Quillora or in a bookstore, they should immediately think:
“This looks like a serious leadership book.”
The design should feel like it belongs next to books by authors such as:
Marcus Dovell
Brant Feltham
Owen Marsh
Peter Halvorn
A strong, confident cover that attracts leaders who want to grow and perform at a higher level.
Updates
Target Market(s)
Business Owners and High level managers
Look and feel

```html
<!DOCTYPE html>
<html lang="en">
<head>
<meta charset="utf-8">
<title>Rise As Captain — Book Cover</title>
<link rel="stylesheet" href="https://fonts.googleapis.com/css2?family=Cinzel:wght@400;500;600&family=League+Gothic&display=swap">
<style>
  :root {
    --backdrop: #333333;
    --paper: #ffffff;
    --title-red: #7e0c0e;
    --window-red: #5a0b0f;
    --window-mid: #7d4a4c;
    --window-haze: #e2e2e2;
    --ink: #141414;
    --subtitle-ink: #f6f0f0;
  }
  html, body {
    margin: 0;
    padding: 0;
    width: 1200px;
    height: 1200px;
    overflow: hidden;
    background: var(--backdrop);
  }
  .canvas {
    position: relative;
    width: 1200px;
    height: 1200px;
    background: var(--backdrop);
  }
  .cover {
    position: absolute;
    left: 210px;
    top: 12px;
    width: 780px;
    height: 1176px;
    background: var(--paper);
    overflow: hidden;
  }
  .title-lead {
    position: absolute;
    top: 52px;
    left: 0;
    width: 100%;
    text-align: center;
    font-family: "Cinzel", serif;
    font-weight: 500;
    color: var(--ink);
    font-size: 52px;
    letter-spacing: 3px;
    line-height: 1;
  }
  .title-lead .initial { font-size: 68px; }
  .title-main {
    position: absolute;
    top: 150px;
    left: 52px;
    width: 676px;
    height: 320px;
  }
  .title-main text {
    font-family: "League Gothic", "Oswald", sans-serif;
    fill: var(--title-red);
  }
  .reveal-artwork {
    position: absolute;
    left: 40px;
    top: 520px;
    width: 710px;
    height: 500px;
    background: radial-gradient(ellipse 50% 50% at 50% 48%,
      var(--window-red) 0%,
      var(--window-red) 62%,
      var(--window-mid) 76%,
      var(--window-haze) 88%,
      var(--paper) 100%);
  }
  .subtitle {
    position: absolute;
    top: 640px;
    left: 0;
    width: 100%;
    text-align: center;
    font-family: "Cinzel", serif;
    font-weight: 500;
    font-size: 46px;
    line-height: 56px;
    letter-spacing: 1px;
    color: var(--subtitle-ink);
    margin: 0;
  }
  .author {
    position: absolute;
    top: 1098px;
    left: 0;
    width: 100%;
    text-align: center;
    font-family: "Cinzel", serif;
    font-weight: 500;
    font-size: 46px;
    line-height: 1;
    letter-spacing: 3px;
    color: var(--ink);
    margin: 0;
  }
</style>
</head>
<body>
<div class="canvas">
  <div class="cover">
    <div class="title-lead"><span class="initial">R</span>ISE AS</div>

    <svg class="title-main" viewBox="0 0 676 320" aria-label="Captain">
      <text x="0" y="318" font-size="420" textLength="676" lengthAdjust="spacingAndGlyphs">CAPTAIN</text>
    </svg>

    <div class="reveal-artwork" role="img" aria-label="Illustration of white paper torn open to reveal a deep red surface"></div>

    <p class="subtitle">THE 12 QUIET<br>PILLARS OF<br>REMARKABLE<br>COMMAND</p>

    <p class="author">ORWEN TALBRISK</p>
  </div>
</div>
</body>
</html>
```